KVR Bastion White Paper

We want our text documents to look professional for advertising purposes. We want the White paper to look similar to our Dornwick Basin Study Document attached.

```html
<!DOCTYPE html>
<html lang="en">
<head>
<meta charset="utf-8">
<title>KVR Bastion White Paper</title>
<link href="https://fonts.googleapis.com/css2?family=Didact+Gothic&family=Mulish:wght@700;800&display=swap" rel="stylesheet">
<style>
:root{
  --backdrop:#7d7d7d;
  --paper:#ffffff;
  --navy:#253a8c;
  --heading:#1f3592;
  --cyan:#00a9e6;
  --ink:#1c1c1c;
  --quote:#2c44a0;
  --rule:#6f7fc0;
}
*{margin:0;padding:0;box-sizing:border-box}
html,body{width:1200px;height:905px;overflow:hidden;background:var(--backdrop)}
body{position:relative;font-family:"Didact Gothic",sans-serif;color:var(--ink)}
.page{position:absolute;width:537px;height:694px;background:var(--paper);overflow:hidden;box-shadow:0 6px 18px rgba(0,0,0,.25)}
.page--one{left:47px;top:28px}
.page--two{left:609px;top:183px}
.page__topband{position:absolute;left:0;top:0;width:100%;height:7px;background:var(--navy)}
.page__footer{position:absolute;left:0;bottom:0;width:100%;height:38px;background:var(--navy)}
.page__number{position:absolute;top:0;width:45px;height:38px;background:var(--cyan);color:#111;font-size:17px;display:flex;align-items:center;justify-content:center}
.page--one .page__number{right:0}
.page--two .page__number{left:0}
.block{position:absolute;left:63px;width:450px}
.body-text p{font-size:8.8px;line-height:10.45px;text-indent:32px}
.body-text p.plain{text-indent:0}
.body-text b{font-family:"Mulish",sans-serif;font-weight:800}
.section-title{font-family:"Mulish",sans-serif;font-weight:800;font-size:11.2px;color:var(--heading);white-space:nowrap}
.section-title--long{font-weight:700;font-size:10.4px;width:460px}
.sub-title{font-family:"Mulish",sans-serif;font-weight:700;font-size:11.8px;color:var(--heading);display:flex;align-items:center;gap:6px;white-space:nowrap}
.sub-title .bullet{width:10px;height:10px;border-radius:50%;background:var(--cyan);flex:none}
.quote-open,.quote-close{position:absolute;font-family:"Mulish",sans-serif;font-weight:800;color:var(--cyan);font-size:58px;line-height:1}
.quote-open{left:61px;top:22px}
.quote-close{left:486px;top:118px}
.quote-text{font-size:8.8px;line-height:10.6px;color:var(--quote)}
.quote-text b{font-family:"Mulish",sans-serif;font-weight:800}
.quote-rule{position:absolute;left:63px;top:155px;width:420px;height:1px;background:var(--rule)}
.notes-rule{position:absolute;left:63px;top:544px;width:450px;height:1px;background:var(--rule)}
.notes{position:absolute;left:59px;top:558px;list-style:none}
.notes li{display:flex;align-items:center;height:16px;font-size:7px;color:var(--navy)}
.notes .num{width:10px;height:10px;border:1px solid var(--navy);border-radius:50%;font-size:6.5px;display:flex;align-items:center;justify-content:center;margin-right:22px}
</style>
</head>
<body>

<article class="page page--one">
  <div class="page__topband"></div>
  <div class="quote-open">&ldquo;</div>
  <div class="block quote-text" style="top:71px">&ldquo;While advances have been made in infection control practices, including improved operating room ventilation, sterilization methods, barriers, surgical techniques, and availability of antimicrobial prophylaxis, SSIs remain a substantial cause of morbidity, prolonged hospitalization, and death. SSI is associated with a mortality rate of <b>3%</b> and <b>75%</b> of SSI associated deaths are directly attributable to SSI.&rdquo; <b>~ NIA i</b></div>
  <div class="block quote-text" style="top:124px;width:420px">&ldquo;More than <b>20,000</b> deaths per year are due to SSIs, and the chance of death in a surgical patient is doubled if an SSI occurs&rdquo; <b>~ Harwell University College of Medicine, Dept. of Surgery ii</b></div>
  <div class="quote-close">&rdquo;</div>
  <div class="quote-rule"></div>

  <h2 class="block section-title" style="top:170px">I. MAJOR SURGICAL SITE INFECTION PROBLEM IN THE U.S.</h2>
  <div class="block body-text" style="top:189px">
    <p>America wastes billions of dollars annually on post-operative surgical site infection expenses, especially related to open abdominal surgeries. Surgical site infection (&ldquo;SSI&rdquo;) slows the recovery rate for patients and adds additional health costs to facilities with prolonged hospital treatment, additional home care, physician office and emergency room visits expenses.</p>
    <p>Open surgeries are more susceptible to high infection rates and slow patient recovery periods which also impact physicians, staff, hospitals, insurers, etc. Moreover, SSI costs hospitals billions of dollars every year in the U.S. and insurance companies do not reimburse hospitals for maladies caused by infection, and corresponding complications due to SSI.</p>
    <p>&ldquo;Surgical site infections (SSI) are among the most common health care-associated infections. Surgical site infections account for 20% to 31% of health care-associated infections in hospitalized patients and have considerable morbidity, a mortality rate of 3%, stays prolonged by 7 to 10 days, and costs <b>$20,000 to $27,000</b> per admission. Reducing SSIs is a national priority, as reflected in the National Department of Health&rsquo;s National Action Plan to Prevent Healthcare-Associated Infections.&rdquo;</p>
    <p class="plain"><b>~ Journal of the Clinical Medicine Association iii</b></p>
  </div>

  <h2 class="block section-title" style="top:355px">II. CURRENT SOLUTIONS</h2>
  <h3 class="block sub-title" style="top:374px"><span class="bullet"></span>Open Wound and Drainage Treatments</h3>
  <div class="block body-text" style="top:392px">
    <p>Surgeons often respond to the high risk of SSI with various open wound and drainage techniques; they do not close the incision area following surgery to allow oxygen into the impacted area. The patient is left with a hole in their body that is open to the outside; restricting patients from normal activity and subjecting them to psychological distress of knowing and often visibly seeing their own open wound. Open wounds require daily wound care cleanings and dressing changes, antibiotics and often high cost wound vac treatments for one to two weeks or longer.</p>
    <p>Physicians, in attempts to avoid an open wound, will often install a drainage device either by cutting an additional incision into the patient or by placing a drain laterally inside the wound. This is accomplished by placing a plastic tube into the patient, horizontally along the fascia layer and closing the wound around the tube. The most common drains -- the <b>&ldquo;J-Drain&rdquo;</b>, and <b>&ldquo;Penrose Drain&rdquo;</b> -- have a tendency to clog up and can even increase the production of additional fluid in patients and consequently the colonization of pathogens, defeating the purpose of the drains. The drains must then be removed by surgeon sometimes a week or more after surgery.</p>
    <p>While antibiotics are useful to patient recoveries and are routinely administered prior to and following surgeries, and in conjunction with other preventative measures, pathogens can adapt to antibiotics which has reduced their effectiveness as a preventive measure.</p>
  </div>

  <h3 class="block sub-title" style="top:577px"><span class="bullet"></span>Negative Pressure Therapy Devices</h3>
  <div class="block body-text" style="top:595px">
    <p>Recently, &ldquo;negative pressure therapy&rdquo; <b>(NPT)</b> devices are often touted as the standard of care for closed incision as well as open wound infection preventative treatments. NPT devices remove excess fluid from surface areas from the outer skin level but can be subject to complications.iv NPT devices are very expensive, physician and nurse-labor intensive, subjected to numerous recalls and often require capital expenditures.</p>
    <p class="plain">In addition, their effectiveness is now being questioned by some clinicians.v</p>
  </div>

  <footer class="page__footer"><div class="page__number">1</div></footer>
</article>

<article class="page page--two">
  <div class="page__topband"></div>

  <h3 class="block sub-title" style="top:27px"><span class="bullet"></span>Wound Packing Techniques</h3>
  <div class="block body-text" style="top:45px">
    <p>In an attempt to protect their patients, some surgeons use various wound packing techniques to varying degrees of success. These physicians are making their own customized materials, cutting strips and soaking them in various solutions in advance of surgery to protect patients from SSI as best they can. Material retention after surgery is also a concern. While these surgeons are implementing their own materials and methods to help protect their patients, acting on their own they could be placing patients and themselves at additional risk due to non-standardized procedures, material retention, and lack of official oversight.</p>
  </div>

  <h2 class="block section-title section-title--long" style="top:127px">III. A New Approach is Needed to Lower Healthcare Costs and Reduce SSI Rates.</h2>
  <h3 class="block sub-title" style="top:151px"><span class="bullet"></span>Wound Packing Study</h3>
  <div class="block body-text" style="top:169px">
    <p><b>Dornwick Basin Health network (&ldquo;Dornwick Study&rdquo;)</b> conducted a clinical trial on the effectiveness of wound packing. The Dornwick Study involved a high-risk patient group in open colon resection surgeries, a high-risk SSI surgery category, involving a detailed wound packing technique developed over years of case studies. The patient group was comprised of individuals with a variety of high SSI risk factors: steroids/immunosuppressants, some contaminated wounds, blood transfusions, more than 50% had stomas, and an average age of <b>65.6</b> and average BMI of <b>29</b>.</p>
    <p>Despite the presence of multiple SSI risk factors and high SSI risk colon sectioning procedures, and the fact that all the patients had their incisions closed with sutures or staples immediately following surgery, the patient group using wound packing resulted in a <b>2.2%</b> overall infection rate, an <b>84%</b> reduction in SSI overall, down from <b>14.2%</b> which was the institution&rsquo;s control SSI rate. The study had only one case of superficial infection in the study group and zero cases of deep tissue infection.</p>
    <p>KVR Bastion&trade; was designed and developed based on the Dornwick Study, and has been patented and cleared by the national health regulator, and is available for use on clean-contaminated and contaminated wounds and adult patients and pediatrics.</p>
  </div>

  <h3 class="block sub-title" style="top:341px"><span class="bullet"></span>Subcutaneous Dressing Technology: KVR Bastion&trade;</h3>
  <div class="block body-text" style="top:360px">
    <p>Subcutaneous dressing technology absorbs fluids from multiple points from the facia layer and above &ndash; along the incision site. The subcutaneous dressing transports fluid and debris external to the body and absorbed into the dressing on top of the wound. After the subcutaneous device is removed, the fistulae created by the device forms a channel for the removal of additional fluids and debris.</p>
    <p>KVR Bastion&trade; device is a single-use disposable that features surgical packing strips that are treated with anti-MRSA PHMB Polyhexamethlene Biguanide. With the device, the surgical strips are physically attached to a silver alginate dressing. KVR Bastion&trade; is made in the United States.</p>
    <p>KVR Bastion&trade; is applied on patients only once immediately following surgery. Packing strips are inserted into the wound and is removed two days later. After that only light dressings and standard wound cleaning methods are employed.</p>
    <p>The device can used for clean-contaminated and contaminated incisions. Extra incisions are not needed in the patient, open wound procedures are used only infrequently, and capital rentals and purchases are eliminated.</p>
    <p>KVR Bastion can be used on a partial procedure listing including abdominal, trauma and many cancer surgeries, stomach and digestive tract, gallbladder, small intestine, large intestine, appendix, liver, pancreas, esophagus, colon, bladder, prostate, uterus, ovaries, kidney, caesarian section and pediatric procedures.</p>
  </div>

  <div class="notes-rule"></div>
  <ol class="notes">
    <li><span class="num">1</span>https://www.nia-health.org/pdfs/manual/site-infection-current.pdf</li>
    <li><span class="num">2</span>https://harwell.edu/medicine/departments/surgery/research/surgical-infections/</li>
    <li><span class="num">3</span>https://jcma-journal.org/articles/clinical/fullarticle/4471203</li>
    <li><span class="num">4</span>http://www.woundcare-review.org/data/editor/NPWT-types-uses-and-possible-complications.pdf</li>
    <li><span class="num">5</span>https://medresearch-methods.org/articles/10.5521/2210-3381-8-4</li>
  </ol>

  <footer class="page__footer"><div class="page__number">2</div></footer>
</article>

</body>
</html>
```